Website Home Page for Women's Health Medical Office

Redesign existing homepage for website using existing logo. Current website location is www.lumawomenscare.com. Please give it a modern, streamlined, playful feel.

Please give it a feminine feel and make it bright and cheerful using logo colors.

Target Market(s)

Women between the ages of 25-45

Industry/Entity Type

Medical Office

Coding

Coded - Design and coding required

Number of Pages Required

1 page

Font styles to use
Sans Serif
Other font styles liked:
• SEGOI UI script for text and GIL SANS for bold (or their equivilent)

Colors
E54698
E96AAD
F1A4CE
F9D9EA
FCEFF6

Requirements
Must have
• Existing logo. Logo Colors. Feminine, cheerful, simple design. all relevant contact information
Nice to have
• clean lines and streamlined look
Should not have
• Cluttered

```html
<!DOCTYPE html>
<html lang="en">
<head>
<meta charset="utf-8">
<title>Luma OB/GYN – Personalized Medical Care for Women</title>
<link rel="stylesheet" href="https://fonts.googleapis.com/css2?family=Montserrat:wght@800;900&family=Open+Sans:ital,wght@0,300;0,400;0,600;0,700;1,300&display=swap">
<style>
:root{
  --pink:#f0067f;
  --pink-soft:#e54698;
  --blush:#f6eef3;
  --lilac:#e8d8e3;
  --ink:#151515;
  --text:#555;
  --white:#fff;
  --dark:#262626;
}
*{box-sizing:border-box;margin:0;padding:0}
html,body{width:1200px;height:4203px;overflow:hidden;background:var(--white)}
body{font-family:"Open Sans",Arial,sans-serif;color:var(--text);position:relative}
.btn{position:absolute;display:flex;align-items:center;justify-content:center;border-radius:40px;font-family:"Open Sans",sans-serif;font-weight:700;font-size:17px;text-transform:uppercase;letter-spacing:.2px;text-decoration:none}
.btn-pink{background:var(--pink);color:var(--white)}
.btn-white{background:var(--white);color:var(--ink)}
.display{font-family:"Montserrat",sans-serif;font-weight:900;text-transform:uppercase;letter-spacing:1px;color:var(--ink)}
.tagline{font-family:"Open Sans",sans-serif;font-style:italic;font-weight:300}
.body-copy{font-size:14.5px;line-height:25.5px;color:var(--text)}

/* header */
.site-header{position:absolute;top:0;left:0;width:1200px;height:114px;background:var(--white);z-index:3}
.contact-bar{position:absolute;right:110px;top:22px;font-size:15px;color:#444;display:flex;gap:14px;align-items:center}
.contact-bar svg{width:13px;height:13px;fill:var(--pink);vertical-align:-1px;margin-right:5px}
.main-nav{position:absolute;right:110px;top:77px;display:flex;gap:24px;font-size:16px;color:#333;text-transform:uppercase}
.main-nav .active{color:var(--pink)}
.logo-badge{position:absolute;left:82px;top:-30px;width:270px;height:266px;border-radius:50%;background:var(--white);z-index:4;display:flex;flex-direction:column;align-items:center;justify-content:center;padding-top:40px}
.logo-mark{width:60px;height:60px;border-radius:50%;border:3px solid var(--pink);margin-bottom:12px}
.logo-name{font-family:"Open Sans",sans-serif;font-weight:700;font-size:26px;color:var(--pink)}

/* hero */
.hero{position:absolute;top:114px;left:0;width:1200px;height:690px;background:linear-gradient(180deg,#b07ab8 0%,#a24aa6 45%,#7d2f8a 100%);overflow:hidden}
.hero-model{position:absolute;right:170px;top:20px;width:330px;height:670px;background:linear-gradient(180deg,#c9a59a 0%,#9cc3e6 40%,#8bb6e0 100%);border-radius:160px 160px 0 0;opacity:.85}
.hero .tagline{position:absolute;left:111px;top:146px;font-size:30px;color:var(--white)}
.hero h1{position:absolute;left:108px;top:200px;font-size:58px;line-height:62px;color:var(--white)}
.hero .btn{left:111px;top:367px;width:266px;height:68px}
.hero-wave{position:absolute;left:0;top:640px;z-index:2}

/* welcome */
.welcome-photo{position:absolute;left:90px;top:709px;width:456px;height:615px;background:radial-gradient(ellipse at 50% 35%,#e9c9b5 0%,#d8b48f 35%,#3a3533 75%);border-radius:46% 46% 0 0;z-index:2}
.welcome-text{position:absolute;left:620px;top:856px;width:470px}
.welcome-text h2{font-size:35px;line-height:47px}
.welcome-text p{margin-top:20px}
.welcome .btn{left:620px;top:1198px;width:162px;height:62px}

/* services */
.services{position:absolute;top:1324px;left:0;width:1200px;height:792px;background:var(--blush);overflow:hidden}
.services h2{position:absolute;left:111px;top:62px;font-size:33px}
.services-art{position:absolute;right:0;top:0;width:400px;height:792px;background:radial-gradient(ellipse at 60% 55%,#dcc4d4 0%,var(--lilac) 60%,var(--blush) 100%);border-radius:60% 0 0 40%}
.service{position:absolute;left:111px;width:680px}
.service-icon{position:absolute;left:0;top:0;width:137px;height:137px;border-radius:50%;background:var(--white);box-shadow:0 4px 14px rgba(0,0,0,.08);display:flex;align-items:center;justify-content:center}
.service-icon svg{width:62px;height:62px;fill:none;stroke:var(--pink);stroke-width:3;stroke-linecap:round;stroke-linejoin:round}
.service h3{position:absolute;left:160px;top:20px;font-weight:400;font-size:22px;color:var(--ink)}
.service p{position:absolute;left:161px;top:62px;width:510px}

/* specialists */
.specialist-photo{position:absolute;left:90px;top:2168px;width:484px;height:562px;border-radius:50%;background:radial-gradient(circle at 45% 40%,#e7c2a6 0%,#8aa5b8 45%,#6f8aa0 100%)}
.specialists-text{position:absolute;left:636px;top:2210px;width:460px}
.specialists-text h2{font-size:35px;line-height:47px}
.specialists-text p{margin-top:24px}
.specialists .btn{left:636px;top:2611px;width:162px;height:62px}
.specialists-art{position:absolute;left:815px;top:2584px;width:342px;height:423px;z-index:3}

/* cta */
.cta-wave{position:absolute;left:0;top:2780px;z-index:1}
.cta .tagline{position:absolute;left:111px;top:2878px;font-size:30px;color:var(--white);z-index:2}
.cta h2{position:absolute;left:110px;top:2940px;font-size:48px;line-height:57px;color:var(--white);z-index:2}
.cta-line{position:absolute;left:111px;top:3069px;font-size:21px;color:var(--white);z-index:2}
.cta-line strong{font-style:italic;font-weight:700}
.cta .btn{left:111px;top:3136px;width:266px;height:68px;z-index:2}

/* insurance */
.insurance{position:absolute;top:3265px;left:0;width:1200px;height:540px;background:var(--white)}
.insurance-photo{position:absolute;left:0;top:0;width:685px;height:540px;background:linear-gradient(90deg,#f0ece9 0%,#d9c6bb 50%,#f7f5f4 100%)}
.plan-list{position:absolute;top:58px;list-style:none;font-size:14.5px;color:#555}
.plan-list li{height:29px;display:flex;align-items:center;white-space:nowrap}
.plan-list svg{width:13px;height:13px;fill:var(--pink);margin-right:6px}
.plans-a{left:696px}
.plans-b{left:926px}

/* footer */
.footer-wave{position:absolute;left:0;top:3690px;z-index:2}
.site-footer{position:absolute;top:3800px;left:0;width:1200px;height:403px;background:var(--dark);color:var(--white);z-index:2}
.footer-brand{position:absolute;left:106px;top:40px;width:318px;height:200px;display:flex;flex-direction:column;align-items:center;justify-content:center}
.footer-brand .logo-mark{width:70px;height:70px}
.footer-brand .logo-name{font-size:32px;color:var(--white)}
.footer-col{position:absolute;top:66px}
.footer-col h4{font-size:18px;font-weight:700;margin-bottom:16px}
.footer-col li{list-style:none;font-size:15px;line-height:27.5px}
.quick-links{left:570px}
.contact-info{left:784px}
.contact-info li{display:flex;gap:12px;margin-bottom:26px;line-height:27px}
.contact-info svg{width:13px;height:13px;fill:var(--pink);margin-top:7px;flex:none}
.footer-rule{position:absolute;left:111px;top:300px;width:978px;height:1px;background:#4a4a4a}
.copyright{position:absolute;left:111px;top:340px;font-size:15px}
.social{position:absolute;left:962px;top:333px;display:flex;gap:8px}
.social span{width:37px;height:37px;border-radius:50%;border:2px solid var(--pink)}
</style>
</head>
<body>

<header class="site-header">
  <div class="contact-bar">
    <span><svg viewBox="0 0 24 24"><path d="M6.6 10.8a15.1 15.1 0 0 0 6.6 6.6l2.2-2.2c.3-.3.7-.4 1-.2 1.1.4 2.3.6 3.6.6.6 0 1 .4 1 1V20c0 .6-.4 1-1 1A17 17 0 0 1 3 4c0-.6.4-1 1-1h3.5c.6 0 1 .4 1 1 0 1.3.2 2.5.6 3.6.1.3 0 .7-.2 1z"/></svg>(555) 014-2290</span>
    <span>|</span>
    <span><svg viewBox="0 0 24 24"><path d="M2 5h20v14H2z M2 5l10 8 10-8" stroke="#fff" stroke-width="1.5"/></svg>admin@lumawomenscare.com</span>
  </div>
  <nav class="main-nav"><span class="active">Home</span><span>Services</span><span>Resources</span><span>About Us</span><span>Contact Us</span></nav>
</header>
<div class="logo-badge"><span class="logo-mark"></span><span class="logo-name">Luma OB/GYN</span></div>

<section class="hero">
  <div class="hero-model" role="img" aria-label="Smiling expectant mother in a light blue dress standing in a lavender field"></div>
  <p class="tagline">Personalized medical care for woman</p>
  <h1 class="display">Better Health<br>Starts Here!</h1>
  <a class="btn btn-pink">Make an Appointment</a>
</section>
<svg class="hero-wave" width="1200" height="164" viewBox="0 0 1200 164"><path d="M0 86 C180 20 330 0 560 40 C760 75 900 150 1200 156 L1200 164 L0 164Z" fill="#fff"/></svg>

<section class="welcome">
  <div class="welcome-photo" role="img" aria-label="Portrait of a smiling blonde physician"></div>
  <div class="welcome-text">
    <h2 class="display">Welcome to Luma<br>OB/GYN, Fairview, CA</h2>
    <p class="body-copy">At Luma OB/GYN in Fairview, California, we believe better health starts when the patient is educated. For this reason, we take time to listen to our patients concerns, explain each option available, and to answer any questions our patients may have so that they can make informed decisions. At Luma OB/GYN, our providers tailor every procedure performed and treatment option recommended to meet the specific needs of our patients.</p>
  </div>
  <a class="btn btn-pink">Read More</a>
</section>

<section class="services">
  <div class="services-art" role="img" aria-label="Soft line silhouette of a pregnant woman with a pink heart"></div>
  <h2 class="display">How can we help you?</h2>
  <div class="service" style="top:132px">
    <div class="service-icon"><svg viewBox="0 0 64 64"><circle cx="32" cy="14" r="7"/><path d="M26 24c-4 10 0 16 10 20s4 14-4 16"/></svg></div>
    <h3>Pregnancy Care</h3>
    <p class="body-copy">Receiving regular care in pregnancy is important for the health of both you and your baby. Our obstetricians work with you every step of the way during your pregnancy and delivery..</p>
  </div>
  <div class="service" style="top:286px">
    <div class="service-icon"><svg viewBox="0 0 64 64"><path d="M6 40h52M32 40c-10-8-10-22 0-22s10 14 0 22z"/></svg></div>
    <h3>Birth Control Services</h3>
    <p class="body-copy">Our gynecologists are knowledgeable on all forms of birth control including the IUD, hormonal implant, vaginal ringinsertion, birth control pills, and more! ..</p>
  </div>
  <div class="service" style="top:441px">
    <div class="service-icon"><svg viewBox="0 0 64 64"><rect x="14" y="10" width="36" height="46" rx="4"/><circle cx="32" cy="26" r="6"/><path d="M32 32v8M28 36h8M22 46h20"/></svg></div>
    <h3>Well Woman Exams</h3>
    <p class="body-copy">Our providers will help you to stay healthy by performing a physical exam on you annually. We will screen you for multiple health conditions that may pose a risk to you.</p>
  </div>
  <div class="service" style="top:596px">
    <div class="service-icon"><svg viewBox="0 0 64 64"><circle cx="32" cy="32" r="14"/><path d="M32 24v16M24 32h16M6 46c8 8 20 10 30 4M58 18c-8-8-20-10-30-4"/></svg></div>
    <h3>Women’s Health Issues</h3>
    <p class="body-copy">Whether you are dealing with painful or irregular periods, fibroids, or other women’s health i ssues, we can help. We offer a variety of the most up-to-date treatment options to help you regain your lifestyle.</p>
  </div>
</section>

<section class="specialists">
  <div class="specialist-photo" role="img" aria-label="Nurse in scrubs holding a newborn baby"></div>
  <div class="specialists-text">
    <h2 class="display">Your OB/GYN<br>Specialists</h2>
    <p class="body-copy">Luma OB/GYN offers you the best care possible in a personalized setting. We are currently accepting patients. Call our office now to make an appointment.</p>
    <p class="body-copy">Luma OB/GYN (located near Fairview Springs Hospital in Fairview, CA) is a medical office that specializes in Christ-centered healthcare for women of all ages. Our team of exclusively female providers have years of experience taking care of women with a variety of pregnancy and gynecology concerns.</p>
  </div>
  <a class="btn btn-pink">Read More</a>
  <div class="specialists-art" role="img" aria-label="Pink line drawing of a mother holding her baby" style="background:radial-gradient(ellipse at 50% 55%,rgba(240,6,127,.10) 0%,rgba(240,6,127,0) 70%)"></div>
</section>

<section class="cta">
  <svg class="cta-wave" width="1200" height="485" viewBox="0 0 1200 485"><path d="M0 125 C140 45 300 10 480 18 C700 30 820 210 1200 212 L1200 485 L0 485Z" fill="#f0067f"/></svg>
  <p class="tagline">Better Health Starts Here!</p>
  <h2 class="display">Now Accepting<br>New Patients</h2>
  <p class="cta-line">Click Here for an Appointment or Call Us At <strong>(555) 014-2290</strong></p>
  <a class="btn btn-white">Make an Appointment</a>
</section>

<section class="insurance">
  <div class="insurance-photo" role="img" aria-label="Doctor listening to a pregnant patient's belly with a stethoscope"></div>
  <ul class="plan-list plans-a">
    <li><svg viewBox="0 0 24 24"><path d="M9 16.2 4.8 12l-1.4 1.4L9 19 21 7l-1.4-1.4z"/></svg>Alignwell Plan</li>
    <li><svg viewBox="0 0 24 24"><path d="M9 16.2 4.8 12l-1.4 1.4L9 19 21 7l-1.4-1.4z"/></svg>Inlandia Direct</li>
    <li><svg viewBox="0 0 24 24"><path d="M9 16.2 4.8 12l-1.4 1.4L9 19 21 7l-1.4-1.4z"/></svg>Primewell of Oakdale</li>
    <li><svg viewBox="0 0 24 24"><path d="M9 16.2 4.8 12l-1.4 1.4L9 19 21 7l-1.4-1.4z"/></svg>Primewell of Ridgeview</li>
    <li><svg viewBox="0 0 24 24"><path d="M9 16.2 4.8 12l-1.4 1.4L9 19 21 7l-1.4-1.4z"/></svg>Silverline Plan</li>
    <li><svg viewBox="0 0 24 24"><path d="M9 16.2 4.8 12l-1.4 1.4L9 19 21 7l-1.4-1.4z"/></svg>Harborlane Medical Group</li>
    <li><svg viewBox="0 0 24 24"><path d="M9 16.2 4.8 12l-1.4 1.4L9 19 21 7l-1.4-1.4z"/></svg>ServiceCare Prime</li>
    <li><svg viewBox="0 0 24 24"><path d="M9 16.2 4.8 12l-1.4 1.4L9 19 21 7l-1.4-1.4z"/></svg>Meadowvale Physicians</li>
    <li><svg viewBox="0 0 24 24"><path d="M9 16.2 4.8 12l-1.4 1.4L9 19 21 7l-1.4-1.4z"/></svg>Aster Open Access Select</li>
    <li><svg viewBox="0 0 24 24"><path d="M9 16.2 4.8 12l-1.4 1.4L9 19 21 7l-1.4-1.4z"/></svg>Anchorpoint Select</li>
    <li><svg viewBox="0 0 24 24"><path d="M9 16.2 4.8 12l-1.4 1.4L9 19 21 7l-1.4-1.4z"/></svg>Blue Harborlane</li>
    <li><svg viewBox="0 0 24 24"><path d="M9 16.2 4.8 12l-1.4 1.4L9 19 21 7l-1.4-1.4z"/></svg>Cedarline</li>
    <li><svg viewBox="0 0 24 24"><path d="M9 16.2 4.8 12l-1.4 1.4L9 19 21 7l-1.4-1.4z"/></svg>Cedarline Local Plus</li>
    <li><svg viewBox="0 0 24 24"><path d="M9 16.2 4.8 12l-1.4 1.4L9 19 21 7l-1.4-1.4z"/></svg>Veteran Family Plan</li>
  </ul>
  <ul class="plan-list plans-b">
    <li><svg viewBox="0 0 24 24"><path d="M9 16.2 4.8 12l-1.4 1.4L9 19 21 7l-1.4-1.4z"/></svg>Benefitry</li>
    <li><svg viewBox="0 0 24 24"><path d="M9 16.2 4.8 12l-1.4 1.4L9 19 21 7l-1.4-1.4z"/></svg>Federal Staff Plan</li>
    <li><svg viewBox="0 0 24 24"><path d="M9 16.2 4.8 12l-1.4 1.4L9 19 21 7l-1.4-1.4z"/></svg>Wellbridge West</li>
    <li><svg viewBox="0 0 24 24"><path d="M9 16.2 4.8 12l-1.4 1.4L9 19 21 7l-1.4-1.4z"/></svg>Crestview Health</li>
    <li><svg viewBox="0 0 24 24"><path d="M9 16.2 4.8 12l-1.4 1.4L9 19 21 7l-1.4-1.4z"/></svg>Steel Trades Trust Fund</li>
    <li><svg viewBox="0 0 24 24"><path d="M9 16.2 4.8 12l-1.4 1.4L9 19 21 7l-1.4-1.4z"/></svg>Builders Health &amp; Welfare Fund</li>
    <li><svg viewBox="0 0 24 24"><path d="M9 16.2 4.8 12l-1.4 1.4L9 19 21 7l-1.4-1.4z"/></svg>Postal Carriers Plan</li>
    <li><svg viewBox="0 0 24 24"><path d="M9 16.2 4.8 12l-1.4 1.4L9 19 21 7l-1.4-1.4z"/></svg>Crane Operators Plan</li>
    <li><svg viewBox="0 0 24 24"><path d="M9 16.2 4.8 12l-1.4 1.4L9 19 21 7l-1.4-1.4z"/></svg>Metal Trades Workers</li>
    <li><svg viewBox="0 0 24 24"><path d="M9 16.2 4.8 12l-1.4 1.4L9 19 21 7l-1.4-1.4z"/></svg>ServiceCare Select</li>
    <li><svg viewBox="0 0 24 24"><path d="M9 16.2 4.8 12l-1.4 1.4L9 19 21 7l-1.4-1.4z"/></svg>Tandemcare Health</li>
    <li><svg viewBox="0 0 24 24"><path d="M9 16.2 4.8 12l-1.4 1.4L9 19 21 7l-1.4-1.4z"/></svg>Grocers Union Plan</li>
    <li><svg viewBox="0 0 24 24"><path d="M9 16.2 4.8 12l-1.4 1.4L9 19 21 7l-1.4-1.4z"/></svg>Plancraft Admin</li>
    <li><svg viewBox="0 0 24 24"><path d="M9 16.2 4.8 12l-1.4 1.4L9 19 21 7l-1.4-1.4z"/></svg>Primewell of Sun City</li>
  </ul>
</section>

<svg class="footer-wave" width="1200" height="112" viewBox="0 0 1200 112"><path d="M0 0 C200 70 420 120 700 100 C900 85 1050 70 1200 100 L1200 112 L0 112Z" fill="#262626"/></svg>
<footer class="site-footer">
  <div class="footer-brand"><span class="logo-mark"></span><span class="logo-name">Luma OB/GYN</span></div>
  <div class="footer-col quick-links">
    <h4>Quick Links</h4>
    <ul><li>Home</li><li>About Us</li><li>News</li><li>Patient Resources</li><li>Privacy Policy</li><li>Contact Us</li></ul>
  </div>
  <div class="footer-col contact-info">
    <h4>Contact Information</h4>
    <ul>
      <li><svg viewBox="0 0 24 24"><path d="M6.6 10.8a15.1 15.1 0 0 0 6.6 6.6l2.2-2.2c.3-.3.7-.4 1-.2 1.1.4 2.3.6 3.6.6.6 0 1 .4 1 1V20c0 .6-.4 1-1 1A17 17 0 0 1 3 4c0-.6.4-1 1-1h3.5c.6 0 1 .4 1 1 0 1.3.2 2.5.6 3.6.1.3 0 .7-.2 1z"/></svg>(555) 014-2290</li>
      <li><svg viewBox="0 0 24 24"><path d="M2 5h20v14H2z"/></svg>admin@lumawomenscare.com</li>
      <li><svg viewBox="0 0 24 24"><path d="M12 2a7 7 0 0 0-7 7c0 5 7 13 7 13s7-8 7-13a7 7 0 0 0-7-7zm0 9.5a2.5 2.5 0 1 1 0-5 2.5 2.5 0 0 1 0 5z"/></svg>4180 Meadowlark Avenue, Suite 210,<br>Fairview, CA 90210</li>
    </ul>
  </div>
  <div class="footer-rule"></div>
  <p class="copyright">Copyright © 2022, Luma OB/GYN. All rights reserved.</p>
  <div class="social"><span></span><span></span><span></span></div>
</footer>

</body>
</html>
```